Lotus Leaf Kitchen Road Billboard

Road Billboard I need all of this information on it
Authentic Thai Food Bangkok Style
6.5 Miles on the right
4126 Maple Ridge Rd Otto NC
828-555-4172

```html
<!DOCTYPE html>
<html lang="en">
<head>
<meta charset="utf-8">
<title>Lotus Leaf Kitchen – Road Billboard</title>
<link href="https://fonts.googleapis.com/css2?family=Chonburi&family=Sriracha&family=Fira+Sans:wght@500;600&display=swap" rel="stylesheet">
<style>
  :root {
    --page: #e9e9ea;
    --board: #1a1411;
    --board-edge: #0d0a08;
    --gold: #f0b923;
    --cream: #f4ece0;
    --flame: #e8731c;
    --ember: #9c3a0c;
  }
  * { box-sizing: border-box; margin: 0; padding: 0; }
  html, body {
    width: 1200px; height: 800px; overflow: hidden;
    background: var(--page);
  }
  .billboard {
    position: absolute; left: 20px; top: 110px;
    width: 1160px; height: 580px;
    background: radial-gradient(ellipse at 30% 40%, #2a1e17 0%, var(--board) 60%, var(--board-edge) 100%);
    overflow: hidden;
  }
  .dish-photo {
    position: absolute; left: 600px; top: 30px;
    width: 550px; height: 500px;
    background:
      radial-gradient(ellipse at 52% 30%, #7f9a3a 0%, rgba(127,154,58,0) 22%),
      radial-gradient(ellipse at 22% 40%, var(--flame) 0%, rgba(232,115,28,0) 30%),
      radial-gradient(ellipse at 70% 82%, var(--flame) 0%, rgba(232,115,28,0) 28%),
      radial-gradient(ellipse at 50% 58%, #3a3330 0%, rgba(58,51,48,0) 48%),
      radial-gradient(ellipse at 40% 50%, var(--ember) 0%, rgba(156,58,12,0) 60%);
  }
  .headline {
    position: absolute; left: 62px; top: 48px;
    font-family: "Chonburi", serif;
    color: var(--gold);
    font-size: 80px; line-height: 100px;
    letter-spacing: 1px;
  }
  .headline span { display: block; }
  .headline .line-two { font-size: 86px; }
  .tagline {
    position: absolute; left: 118px; top: 262px;
    font-family: "Sriracha", cursive;
    color: var(--gold);
    font-size: 60px;
    transform: rotate(-2deg);
  }
  .brand {
    position: absolute; left: 52px; top: 486px;
    display: flex; align-items: center; gap: 10px;
    font-family: "Fira Sans", sans-serif; font-weight: 500;
    font-size: 24px; color: var(--gold);
  }
  .brand .mark {
    width: 16px; height: 16px; border-radius: 50%;
    background: var(--gold);
  }
  .directions {
    position: absolute; left: 298px; top: 388px;
    display: flex; align-items: center; gap: 10px;
    font-family: "Fira Sans", sans-serif; font-weight: 600;
    font-size: 56px; color: var(--cream);
  }
  .directions svg { width: 52px; height: 40px; margin-top: 6px; }
  .contact {
    position: absolute; left: 298px; top: 478px; right: 20px;
    display: flex; justify-content: space-between;
    font-family: "Fira Sans", sans-serif; font-weight: 600;
    font-size: 38px; color: var(--cream);
  }
</style>
</head>
<body>
  <main class="billboard">
    <div class="dish-photo" role="img" aria-label="Shrimp and vegetables tossed above a flaming wok with sparks"></div>

    <h1 class="headline">
      <span class="line-one">AUTHENTIC</span>
      <span class="line-two">THAI FOOD</span>
    </h1>
    <p class="tagline">Bangkok Style</p>

    <div class="brand"><span class="mark"></span>Lotus Leaf Kitchen</div>

    <p class="directions">6.5 Miles on the Right
      <svg viewBox="0 0 52 40" aria-hidden="true">
        <path d="M4 20 H40 M26 6 L42 20 L26 34" fill="none" stroke="var(--gold)" stroke-width="8" stroke-linecap="round" stroke-linejoin="round"/>
      </svg>
    </p>

    <div class="contact">
      <span class="address">4126 Maple Ridge Rd, Otto NC</span>
      <span class="phone">828-555-4172</span>
    </div>
  </main>
</body>
</html>
```